Capacity building in Resource Management

Need design of a business card (later to be completed by letterhead and webdesign in same fashion) for a professional who works in the field of capacity building of professionals in mostly developing countries in the field waste/resource management, waste prevention/reduction, cleaner production, stakeholders involvement, etc.
Info on business cards is to include provided logo, info in provided file and picture.

Industry/Entity Type

Business

Contact Information for Business Card

White background

Font styles to use
Sans Serif

Colors

Designer to choose colors to be used in the design.

```html
<!DOCTYPE html>
<html lang="en">
<head>
<meta charset="utf-8">
<title>Business Card – Jorien Vandeberg</title>
<link href="https://fonts.googleapis.com/css2?family=Domine:wght@400;700&display=swap" rel="stylesheet">
<style>
  :root {
    --bg: #e6e7e9;
    --card: #ffffff;
    --ink: #141414;
    --brand-green: #2f8a35;
    --photo-light: #9fb892;
    --photo-dark: #4f6446;
    --shadow: rgba(0, 0, 0, 0.14);
  }
  * { margin: 0; padding: 0; box-sizing: border-box; }
  html, body {
    width: 1200px;
    height: 745px;
    overflow: hidden;
    background: var(--bg);
  }
  .canvas {
    position: relative;
    width: 1200px;
    height: 745px;
    display: flex;
    align-items: center;
    justify-content: center;
  }
  .business-card {
    position: relative;
    width: 1040px;
    height: 594px;
    background: var(--card);
    display: flex;
    box-shadow: 0 10px 30px var(--shadow);
  }
  .portrait {
    width: 390px;
    height: 100%;
    background: linear-gradient(160deg, var(--photo-light) 0%, #7e9a72 45%, var(--photo-dark) 100%);
  }
  .details {
    flex: 1;
    padding: 62px 64px 0 40px;
    display: flex;
    flex-direction: column;
    align-items: flex-end;
    text-align: right;
    font-family: "Domine", serif;
    color: var(--ink);
  }
  .brand {
    display: flex;
    align-items: center;
    gap: 14px;
    font-size: 40px;
    font-weight: 700;
    color: var(--brand-green);
    line-height: 1;
  }
  .brand-mark {
    width: 30px;
    height: 30px;
    background: var(--brand-green);
  }
  .person-name {
    margin-top: 26px;
    font-size: 44px;
    font-weight: 400;
    letter-spacing: 1px;
    text-transform: uppercase;
    line-height: 1.1;
  }
  .contact-list {
    list-style: none;
    margin-top: 28px;
    font-size: 23px;
    line-height: 1.32;
  }
  .address {
    margin-top: 22px;
    font-style: normal;
    font-size: 23px;
    line-height: 1.32;
  }
</style>
</head>
<body>
  <main class="canvas">
    <article class="business-card">
      <div class="portrait" role="img" aria-label="Portrait photo of the consultant in a white shirt by a window with green garden behind"></div>
      <section class="details">
        <div class="brand">
          <span class="brand-mark"></span>
          <span class="brand-name">terra-skills</span>
        </div>
        <h1 class="person-name">Jorien Vandeberg</h1>
        <ul class="contact-list">
          <li>jorien.vandeberg@terra-skills.org</li>
          <li>www.terra-skills.org</li>
          <li>+49 1520 000 4417</li>
          <li>Twitter: @jorienvdberg</li>
          <li>Skype: jvdberg2010</li>
          <li>LinkedIn: Jorien Vandeberg</li>
        </ul>
        <address class="address">
          Lindenweg 12<br>
          10117 Berlin<br>
          Germany
        </address>
      </section>
    </article>
  </main>
</body>
</html>
```